Modern business card design for professional copywriter

I'd like a business card design that I can use to have my cards printed out by plink.com as a squared corners business card (see artwork and design guidelines here: https://help.plink.com/hc/en-gb/sections/300481726-PLINK-Product-Templates)

The design should be clean and modern and reflect the colours, tone and branding on my website: https://noravestrel.com.au

Target Market(s)

Professionals, B2B small business owners

Industry/Entity Type

Business

Contact Information for Business Card

Nora Vestrel
m: 0427 593 864
e: nora@noravestrel.com.au
w: noravestrel.com.au

Font styles to use
Sans Serif

Requirements
Must have
• Tagline: "Smart copywriting for clever business people"
• Brand colours: fd8000, 009984, 666666 and black
Nice to have

```html
<!DOCTYPE html>
<html lang="en">
<head>
<meta charset="utf-8">
<title>Nora Vestrel – Business Card</title>
<link rel="stylesheet" href="https://fonts.googleapis.com/css2?family=Jost:wght@400;500&family=Oswald:wght@500&display=swap">
<style>
  :root {
    --orange: #fd8000;
    --teal: #009984;
    --grey: #666666;
    --black: #000000;
    --paper: #ffffff;
    --backdrop: #efede8;
  }
  * { box-sizing: border-box; margin: 0; padding: 0; }
  html, body {
    width: 1200px; height: 929px; overflow: hidden;
    background: var(--backdrop);
  }
  .stage {
    width: 1200px; height: 929px;
    display: flex; flex-direction: column;
    align-items: center; justify-content: center; gap: 44px;
  }
  .card {
    width: 630px; height: 360px;
    background: var(--paper);
    box-shadow: 0 6px 14px rgba(0,0,0,0.18);
    position: relative;
  }

  /* Front */
  .card--front { display: flex; align-items: center; justify-content: center; }
  .brand { display: flex; align-items: center; gap: 14px; }
  .brand__dot { width: 22px; height: 22px; border-radius: 50%; background: var(--orange); }
  .brand__name {
    font-family: "Jost", sans-serif; font-weight: 500;
    font-size: 52px; color: var(--teal); letter-spacing: -0.5px;
  }

  /* Back */
  .card--back { padding: 0; }
  .identity {
    position: absolute; left: 150px; top: 128px;
    text-align: right; width: 170px;
  }
  .identity__name {
    font-family: "Oswald", sans-serif; font-weight: 500;
    font-size: 34px; line-height: 1; color: var(--teal);
    letter-spacing: 0.5px;
  }
  .identity__role {
    font-family: "Jost", sans-serif; font-size: 17px;
    color: var(--teal); letter-spacing: 0.8px; margin-top: 2px;
  }
  .divider {
    position: absolute; left: 338px; top: 116px;
    width: 2px; height: 74px; background: var(--orange);
  }
  .contacts {
    position: absolute; left: 358px; top: 114px;
    list-style: none;
    font-family: "Jost", sans-serif; font-size: 15.5px;
    color: var(--grey); letter-spacing: 0.6px;
  }
  .contacts li { display: flex; align-items: center; gap: 10px; height: 26px; }
  .contacts svg { width: 13px; height: 13px; flex: none; }
  .tagline {
    position: absolute; left: 0; right: 0; bottom: 62px;
    text-align: center;
    font-family: "Jost", sans-serif; font-size: 16px;
    color: var(--grey); letter-spacing: 1px;
  }
</style>
</head>
<body>
<main class="stage">
  <section class="card card--front" aria-label="Card front">
    <div class="brand">
      <span class="brand__dot"></span>
      <span class="brand__name">Nora Vestrel</span>
    </div>
  </section>

  <section class="card card--back" aria-label="Card back">
    <div class="identity">
      <div class="identity__name">NORA VESTREL</div>
      <div class="identity__role">Copywriter</div>
    </div>
    <span class="divider"></span>
    <ul class="contacts">
      <li>
        <svg viewBox="0 0 14 14" aria-hidden="true"><rect x="3.5" y="1" width="7" height="12" rx="1.2" fill="none" stroke="var(--teal)" stroke-width="1.4"/><line x1="6" y1="11" x2="8" y2="11" stroke="var(--teal)" stroke-width="1.2"/></svg>
        0427 593 864
      </li>
      <li>
        <svg viewBox="0 0 14 14" aria-hidden="true"><rect x="1" y="3" width="12" height="8.5" rx="1" fill="var(--teal)"/><path d="M1.5 3.6 L7 8 L12.5 3.6" fill="none" stroke="#fff" stroke-width="1.2"/></svg>
        nora@noravestrel.com.au
      </li>
      <li>
        <svg viewBox="0 0 14 14" aria-hidden="true"><circle cx="6" cy="6" r="4" fill="none" stroke="var(--teal)" stroke-width="1.8"/><line x1="9" y1="9" x2="13" y2="13" stroke="var(--teal)" stroke-width="2"/></svg>
        noravestrel.com.au
      </li>
    </ul>
    <p class="tagline">Smart copywriting for clever business people</p>
  </section>
</main>
</body>
</html>
```